CD Cover Artwork for Classical Music Cover

We are about to launch 13 CDs online for digital downloads and require artwork for the accompanying CD covers. As the covers will not be printed, we only require web-optimized artwork. We are fine with one standard template that can be adapted for all the covers. The only differentiating factors will be the colour of the covers and the title information. We need to create a more progressive, eye-catching design than the below examples which we have been promoting through our website until now. You have full liberties to come up with whatever design you think is more appropriate and to use whatever fonts and juxtaposition of content and images as you see fit.
ARTIST INFORMATION: Harold Venmark was an American composer who lived and worked his entire life in New York City. He was a 1930 Marlowe Conservatory graduate and studied composition with Milton Brasher, Lew Doddard, Pemberton Quillock and Walter Pennimore. In a 1947 competition, with Karl Estergaard as one of three jurors, Venmark’s "Harbor Prelude" won First Prize. He produced a large body of work comprising hundreds of compositions across diverse musical genres ... From 2001 to early 2008, Harold Venmark’s music came to life through a unique collaboration with many of the finest musicians in St. Petersburg, Russia. Nearly all of Venmark’s musical repertoire was transcribed from their original manuscripts to electronic form. And dozens of recording sessions produced 13 CDs, including all his chambers works, many piano concertos and symphonies, and works for horn, flute, strings and woodwinds. This “musical discovery” was the brainchild of his late son, Thomas Venmark.
ARTIST WEBSITE: www.haroldvenmark.com
FACEBOOK PAGE: https://www.facebook.com/pages/Harold-Venmark-A-Hidden-Chapter-of-Concert-Song/582910374615208
ATTACHMENTS:
- A few images of Harold Venmark (young and old)
- List of CD information along with a visual representation of the information that should be included
Target Market(s)
Classical music lovers the world over
Industry/Entity Type
Electronic
Look and feel

```html
<!DOCTYPE html>
<html lang="en">
<head>
<meta charset="utf-8">
<title>Harold Venmark – A Hidden Chapter of Concert Song – CD Series</title>
<link rel="stylesheet" href="https://fonts.googleapis.com/css2?family=Inter:wght@300;400;600;700;800&display=swap">
<style>
  :root{
    --page:#ffffff;
    --cover:#2e2624;
    --ink:#f3eeea;
    --ink-soft:#d9d2cc;
    --photo-hi:rgba(205,198,192,.85);
    --photo-mid:rgba(120,110,104,.55);
    --c01:#e8a33a; --c02:#e3782a; --c03:#d9572b; --c04:#cc4657;
    --c05:#c84a8c; --c06:#a35ba8; --c07:#8a5ab2; --c08:#7462c0;
    --c09:#5a6cc4; --c10:#3e86c8; --c11:#3a9fa8; --c12:#4f9a6a; --c13:#a7a33a;
  }
  *{margin:0;padding:0;box-sizing:border-box}
  html,body{width:1200px;height:848px;overflow:hidden;background:var(--page)}
  body{position:relative;font-family:"Inter",Arial,sans-serif;color:var(--ink)}

  .cover{position:absolute;background:var(--cover);overflow:hidden}
  .cover .photo{position:absolute;right:0;bottom:0;
    background:radial-gradient(ellipse 48% 50% at 52% 58%,var(--photo-hi) 0%,var(--photo-mid) 38%,rgba(46,38,36,0) 100%)}
  .cover .tag{position:absolute;left:0;top:0;background:var(--accent);color:#fff;font-weight:400}
  .cover .label{position:absolute;font-weight:700;color:#fff;white-space:nowrap}
  .cover .title{position:absolute;font-weight:800;letter-spacing:-0.02em;white-space:nowrap;color:#fff;z-index:1}
  .cover .title span{font-weight:300}
  .cover .subtitle{position:absolute;font-weight:700;color:var(--accent);white-space:nowrap;z-index:1}
  .cover .works{position:absolute;font-weight:300;color:var(--ink-soft);list-style:none;z-index:1;white-space:nowrap}
  .cover .artists{position:absolute;list-style:none;color:var(--ink-soft);font-weight:300;z-index:1;white-space:nowrap}
  .cover .artists b{color:var(--accent);font-weight:600}
  .cover .publisher{position:absolute;font-weight:700;color:#fff;z-index:1}

  /* feature cover */
  .feature{left:80px;top:140px;width:446px;height:446px;--accent:var(--c02);
    box-shadow:6px 8px 14px rgba(0,0,0,.28)}
  .feature .photo{width:330px;height:420px}
  .feature .tag{width:57px;height:38px;font-size:11px;padding:24px 0 0 22px}
  .feature .label{left:64px;top:24px;font-size:11px}
  .feature .title{left:20px;top:86px;font-size:27px}
  .feature .subtitle{left:20px;top:116px;font-size:17px}
  .feature .works{left:20px;top:180px;font-size:12.5px;line-height:17px}
  .feature .artists{left:20px;top:248px;font-size:11px;line-height:15.5px}
  .feature .publisher{left:20px;top:421px;font-size:9.5px}

  /* thumbnails */
  .thumb{width:167px;height:167px;box-shadow:2px 3px 6px rgba(0,0,0,.22)}
  .thumb .photo{width:124px;height:158px}
  .thumb .tag{width:14px;height:14px;font-size:3.5px;padding:8px 0 0 2px}
  .thumb .label{left:18px;top:6px;font-size:4.5px}
  .thumb .title{left:8px;top:31px;font-size:10px}
  .thumb .subtitle{left:8px;top:43px;font-size:6.5px}
  .thumb .works{left:8px;top:67px;font-size:4.6px;line-height:6.5px}
  .thumb .artists{left:8px;top:97px;font-size:4px;line-height:5.5px}
  .thumb .publisher{left:8px;top:157px;font-size:3.8px}
</style>
</head>
<body>

<section class="cover feature">
  <div class="photo" role="img" aria-label="Black and white portrait of the composer reading a score under a lamp"></div>
  <div class="tag">CD 02</div>
  <div class="label">Works for Horn</div>
  <h1 class="title">HAROLD VENMARK <span>1908-1989</span></h1>
  <p class="subtitle">A hidden chapter of concert song</p>
  <ul class="works">
    <li>Duets for Flute and Horn</li>
    <li>Trio for Horn, Bassoon and Piano</li>
    <li>Concertino for Horn and Orchestra</li>
  </ul>
  <ul class="artists">
    <li><b>Vera Solnikova,</b> Flute</li>
    <li><b>Anton Brevskin,</b> Piano</li>
    <li><b>Oleg Tarmanov,</b> Horn</li>
  </ul>
  <p class="publisher">Calder Row Editions</p>
</section>

<section class="cover thumb" style="left:585px;top:57px;--accent:var(--c01)">
  <div class="photo" role="img" aria-label="Portrait of the composer reading a score"></div>
  <div class="tag">CD 01</div><div class="label">Selected Chamber Works</div>
  <h2 class="title">HAROLD VENMARK <span>1908-1989</span></h2>
  <p class="subtitle">A hidden chapter of concert song</p>
  <ul class="works"><li>Selected Chamber Works</li></ul>
  <p class="publisher">Calder Row Editions</p>
</section>

<section class="cover thumb" style="left:764px;top:57px;--accent:var(--c03)">
  <div class="photo" role="img" aria-label="Portrait of the composer reading a score"></div>
  <div class="tag">CD 03</div><div class="label">Works for Flute</div>
  <h2 class="title">HAROLD VENMARK <span>1908-1989</span></h2>
  <p class="subtitle">A hidden chapter of concert song</p>
  <ul class="works"><li>Sonatas for Solo Flute</li><li>Sonata for Flute and Piano</li><li>Duets for Flute and Horn</li><li>Harrow Lane Suite, Flute and Violin</li></ul>
  <ul class="artists"><li><b>Vera Solnikova,</b> Flute</li><li><b>Anton Brevskin,</b> Piano</li><li><b>Oleg Tarmanov,</b> Violin</li></ul>
  <p class="publisher">Calder Row Editions</p>
</section>

<section class="cover thumb" style="left:943px;top:57px;--accent:var(--c04)">
  <div class="photo" role="img" aria-label="Portrait of the composer reading a score"></div>
  <div class="tag">CD 04</div><div class="label">String and Piano Sonatas</div>
  <h2 class="title">HAROLD VENMARK <span>1908-1989</span></h2>
  <p class="subtitle">A hidden chapter of concert song</p>
  <ul class="works"><li>Two Sonatas for Violin and Piano</li><li>Two Sonatas for Viola and Piano</li><li>Sonatina for Cello and Piano</li><li>Sonatina for Contrabass and Piano</li></ul>
  <ul class="artists"><li><b>Kira Lentova,</b> Violin</li><li><b>Ilya Dorvatko,</b> Viola</li><li><b>Sergei Malkin,</b> Cello</li><li><b>Pavel Drozin,</b> Bass</li><li><b>Lidia Marsenko,</b> Piano</li></ul>
  <p class="publisher">Calder Row Editions</p>
</section>

<section class="cover thumb" style="left:585px;top:238px;--accent:var(--c05)">
  <div class="photo" role="img" aria-label="Portrait of the composer reading a score"></div>
  <div class="tag">CD 05</div><div class="label">Works for Piano</div>
  <h2 class="title">HAROLD VENMARK <span>1908-1989</span></h2>
  <p class="subtitle">A hidden chapter of concert song</p>
  <ul class="works"><li>Sonatas</li><li>Suite 3</li><li>Lanterns Over the Pier</li><li>Piano Concerto</li></ul>
  <ul class="artists"><li><b>Nadia Korvelskaya,</b> Piano</li><li><b>Riverside Chamber Orchestra</b></li><li><b>Yuri Pelkanov,</b> Conductor</li></ul>
  <p class="publisher">Calder Row Editions</p>
</section>

<section class="cover thumb" style="left:764px;top:238px;--accent:var(--c06)">
  <div class="photo" role="img" aria-label="Portrait of the composer reading a score"></div>
  <div class="tag">CD 06</div><div class="label">Works for Viola</div>
  <h2 class="title">HAROLD VENMARK <span>1908-1989</span></h2>
  <p class="subtitle">A hidden chapter of concert song</p>
  <ul class="works"><li>Divertimento for Two Violas</li><li>Sonata Notturna for Viola and Piano</li><li>Petite Suite for Viola and Piano</li><li>16 Songs for Voice, Viola and Piano</li></ul>
  <ul class="artists"><li><b>Ilya Dorvatko,</b> Viola</li><li><b>Yuri Pelkanov,</b> Viola</li><li><b>Anton Brevskin,</b> Piano</li><li><b>Marta Velinova,</b> Soprano</li></ul>
  <p class="publisher">Calder Row Editions</p>
</section>

<section class="cover thumb" style="left:943px;top:238px;--accent:var(--c07)">
  <div class="photo" role="img" aria-label="Portrait of the composer reading a score"></div>
  <div class="tag">CD 07</div><div class="label">Works for Clarinet and Oboes</div>
  <h2 class="title">HAROLD VENMARK <span>1908-1989</span></h2>
  <p class="subtitle">A hidden chapter of concert song</p>
  <ul class="works"><li>Two Sonatas for Clarinet and Piano</li><li>Three Movements for Two Oboes and Piano</li><li>Duets for Two Clarinets</li><li>Divertimento for Wind Quartet</li><li>Sonata for Five Clarinets</li></ul>
  <ul class="artists" style="top:101px"><li><b>D. Orlin, A. Fedrov,</b></li><li><b>A. Lenski, V. Katin,</b></li><li><b>M. Alvin, A. Soltin,</b> Clarinets</li><li><b>A. Tomin,</b> Oboe</li><li><b>A. Brevskin,</b> Piano</li></ul>
  <p class="publisher">Calder Row Editions</p>
</section>

<section class="cover thumb" style="left:585px;top:419px;--accent:var(--c08)">
  <div class="photo" role="img" aria-label="Portrait of the composer reading a score"></div>
  <div class="tag">CD 08</div><div class="label">Works for Piano</div>
  <h2 class="title">HAROLD VENMARK <span>1908-1989</span></h2>
  <p class="subtitle">A hidden chapter of concert song</p>
  <ul class="works"><li>Preludes for Piano</li></ul>
  <ul class="artists" style="top:75px"><li><b>Nadia Korvelskaya,</b> Piano</li></ul>
  <p class="publisher">Calder Row Editions</p>
</section>

<section class="cover thumb" style="left:764px;top:419px;--accent:var(--c09)">
  <div class="photo" role="img" aria-label="Portrait of the composer reading a score"></div>
  <div class="tag">CD 09</div><div class="label">Works for String Quartet, Quintet and Trio</div>
  <h2 class="title">HAROLD VENMARK <span>1908-1989</span></h2>
  <p class="subtitle">A hidden chapter of concert song</p>
  <ul class="works"><li>String Quartets</li><li>Fugues and Other Short Pieces</li><li>Two Works for Oboe, Horn and Strings</li></ul>
  <ul class="artists" style="top:88px"><li><b>Neva Lantern Quartet</b></li><li>E. Sorin</li><li>N. Galin</li><li>D. Varlov</li><li>S. Tomov</li></ul>
  <p class="publisher">Calder Row Editions</p>
</section>

<section class="cover thumb" style="left:943px;top:419px;--accent:var(--c10)">
  <div class="photo" role="img" aria-label="Portrait of the composer reading a score"></div>
  <div class="tag">CD 10</div><div class="label">Selected Chamber Works</div>
  <h2 class="title">HAROLD VENMARK <span>1908-1989</span></h2>
  <p class="subtitle">A hidden chapter of concert song</p>
  <ul class="works"><li>Selected Chamber Works</li></ul>
  <p class="publisher">Calder Row Editions</p>
</section>

<section class="cover thumb" style="left:585px;top:600px;--accent:var(--c11)">
  <div class="photo" role="img" aria-label="Portrait of the composer reading a score"></div>
  <div class="tag">CD 11</div><div class="label">Works for Piano</div>
  <h2 class="title">HAROLD VENMARK <span>1908-1989</span></h2>
  <p class="subtitle">A hidden chapter of concert song</p>
  <ul class="works"><li>Suites for Piano</li><li>Piano Sonata</li><li>Petite Suite du Matin</li><li>Four Weathers</li><li>Other Short Pieces</li></ul>
  <ul class="artists" style="top:103px"><li><b>Nadia Korvelskaya,</b> Piano</li></ul>
  <p class="publisher">Calder Row Editions</p>
</section>

<section class="cover thumb" style="left:764px;top:600px;--accent:var(--c12)">
  <div class="photo" role="img" aria-label="Portrait of the composer reading a score"></div>
  <div class="tag">CD 12</div><div class="label">Works for Piano</div>
  <h2 class="title">HAROLD VENMARK <span>1908-1989</span></h2>
  <p class="subtitle">A hidden chapter of concert song</p>
  <ul class="works"><li>Preludes for Piano</li><li>Piano Sonatas</li><li>Caprice</li><li>Works for Two Pianos</li></ul>
  <ul class="artists"><li><b>Alla Preskova,</b> Piano</li><li><b>Lidia Marsenko,</b> Piano</li><li><b>Dina Marsenko,</b> Piano</li></ul>
  <p class="publisher">Calder Row Editions</p>
</section>

<section class="cover thumb" style="left:943px;top:600px;--accent:var(--c13)">
  <div class="photo" role="img" aria-label="Portrait of the composer reading a score"></div>
  <div class="tag">CD 13</div><div class="label">Orchestral Works</div>
  <h2 class="title">HAROLD VENMARK <span>1908-1989</span></h2>
  <p class="subtitle">A hidden chapter of concert song</p>
  <ul class="works"><li>Symphony 7</li><li>Piano Concertos</li></ul>
  <ul class="artists" style="top:84px"><li><b>Members of the</b></li><li><b>Northern Capital Philharmonic</b></li><li><b>Nadia Korvelskaya,</b> Piano</li></ul>
  <p class="publisher">Calder Row Editions</p>
</section>

</body>
</html>
```